100% West Australian Static Banner

I require a static banner to go on a couple of pages in our website (under development) that highlights that we are a 100% Western Australian Owned & Operated company. I would prefer the banner to be in our company colours (blue shades & grey). I also would like it to be eye catching and modern in design. I have included a 100% West Australian rubber stamp logo to be used as well as including our logo so you know our colours. The banner needs to be 1139 x 350 pixels in size.

Target Market(s)

B2B

Requirements
Must have
• Our rubber stamp 100% West Australian logo
• Modern Eye Catching design
• Blue shaded background
Nice to have
• Shading background similar our logo blue colours
• 100% logo can be reversed out if required or colour changed
• Larger text saying - 100% West Australian Owned & Operated

```html
<!DOCTYPE html>
<html lang="en">
<head>
<meta charset="utf-8">
<title>100% West Australian Owned &amp; Operated</title>
<link rel="stylesheet" href="https://fonts.googleapis.com/css2?family=Open+Sans:wght@700&display=swap">
<style>
  :root {
    --navy: #1f2d5e;
    --map-light: #2e8fd0;
    --map-dark: #1d3f78;
    --dot-blue: #2b86cc;
    --dot-teal: #2bb3a8;
    --brand-blue: #2a8ad6;
    --white: #ffffff;
  }
  html, body {
    margin: 0;
    padding: 0;
    overflow: hidden;
    background: var(--navy);
  }
  .banner {
    position: relative;
    width: 1200px;
    height: 369px;
    background: var(--navy);
    overflow: hidden;
    font-family: "Open Sans", Arial, sans-serif;
  }
  .region-map {
    position: absolute;
    left: 16px;
    top: 47px;
    width: 262px;
    height: 270px;
    border-radius: 18px 40px 30px 60px;
    background: linear-gradient(90deg, var(--map-light) 0%, var(--map-dark) 100%);
  }
  .halftone-band {
    position: absolute;
    left: 270px;
    top: 12px;
    width: 72px;
    height: 308px;
    border-radius: 36px;
    background: linear-gradient(180deg,
      rgba(43,134,204,0.15) 0%,
      var(--dot-blue) 30%,
      var(--dot-teal) 50%,
      var(--dot-blue) 70%,
      rgba(43,134,204,0.15) 100%);
  }
  .headline {
    position: absolute;
    left: 376px;
    top: 108px;
    margin: 0;
    color: var(--white);
    font-size: 45px;
    font-weight: 700;
    line-height: 60px;
    white-space: nowrap;
  }
  .brand {
    position: absolute;
    right: -50px;
    top: 160px;
    display: flex;
    align-items: center;
    gap: 24px;
  }
  .brand-name {
    color: var(--brand-blue);
    font-size: 36px;
    font-weight: 700;
    white-space: nowrap;
    margin-top: 40px;
  }
  .brand-square {
    width: 240px;
    height: 240px;
    background: var(--brand-blue);
  }
</style>
</head>
<body>
  <div class="banner">
    <div class="region-map" role="img" aria-label="Map of Western Australia"></div>
    <div class="halftone-band" role="img" aria-label="Decorative vertical band of small round dots"></div>
    <h1 class="headline">100% West Australian<br>Owned &amp; Operated</h1>
    <div class="brand">
      <span class="brand-name">Westvale Group</span>
      <div class="brand-square"></div>
    </div>
  </div>
</body>
</html>
```